Business Card Design Project

We need a business card design for a relatively new company called Velmar Gear. We design paddle (an outdoor winter sport primarily played in the midwest and east coast) and tennis bags for women and men. Velmar Gear is a lifestyle brand for the next generation country club goers. Our bags merge fashion with functionality and are making country club sports trendier and more fashionable.

I would like to include space for
Name: (will fill this in for employees)
Velmar Gear
Phone: (will do this)
Email:
www.velmargear.example

Would also like to include Chatterbook and Flitter icons.
Please do not use pictures of the bags - this is just to give you an idea of what style bags we sell.

Target Market(s)

30 to 40 year old men and women - luxury market

Industry/Entity Type

Fashion

Requirements
Must have
• Would like the company logo included

```html
<!DOCTYPE html>
<html lang="en">
<head>
<meta charset="utf-8">
<title>Velmar Gear – Business Card</title>
<link rel="stylesheet" href="https://fonts.googleapis.com/css2?family=Josefin+Sans:wght@300&family=Cormorant+Garamond:ital,wght@1,700&display=swap">
<style>
  :root {
    --card-black: #000000;
    --ink-white: #ffffff;
    --stripe-orange: #f2a20c;
    --ball-yellow: #e9b62a;
    --ball-amber: #a86f08;
  }
  * { margin: 0; padding: 0; box-sizing: border-box; }
  html, body {
    width: 1200px; height: 627px; overflow: hidden;
    background: var(--card-black);
  }
  .card {
    position: relative; width: 1200px; height: 627px;
    background: var(--card-black); overflow: hidden;
  }
  .ball-photo {
    position: absolute; left: -60px; top: 380px;
    width: 470px; height: 300px;
    background:
      radial-gradient(ellipse 48% 52% at 30% 55%, var(--ball-yellow) 0%, rgba(200,145,20,.75) 45%, rgba(168,111,8,0) 75%),
      radial-gradient(ellipse 38% 48% at 70% 58%, rgba(233,182,42,.85) 0%, rgba(168,111,8,.4) 50%, rgba(0,0,0,0) 80%);
    filter: blur(4px);
  }
  .brand {
    position: absolute; left: 30px; top: 62px;
    display: flex; align-items: center; gap: 46px;
  }
  .brand-mark {
    width: 150px; height: 150px; border-radius: 50%;
    border: 14px solid var(--ink-white);
  }
  .brand-name {
    font-family: "Josefin Sans", sans-serif; font-weight: 300;
    font-size: 142px; line-height: 1; color: var(--ink-white);
    letter-spacing: 4px; white-space: nowrap; padding-top: 22px;
  }
  .edge-stripes { position: absolute; right: 0; top: 0; }
  .contact {
    position: absolute; left: 180px; width: 890px; top: 270px;
    text-align: center; list-style: none;
    font-family: "Cormorant Garamond", serif; font-style: italic; font-weight: 700;
    font-size: 54px; line-height: 60px; color: var(--ink-white);
    letter-spacing: 1px;
  }
</style>
</head>
<body>
<main class="card">
  <div class="ball-photo" role="img" aria-label="Close-up photo of yellow tennis balls, softly out of focus"></div>

  <header class="brand">
    <span class="brand-mark" aria-hidden="true"></span>
    <h1 class="brand-name">Velmar Gear</h1>
  </header>

  <svg class="edge-stripes" width="60" height="627" viewBox="0 0 60 627" aria-hidden="true">
    <rect x="0" y="0" width="60" height="627" fill="#000"/>
    <rect x="1" y="0" width="59" height="54" fill="var(--stripe-orange)"/>
    <rect x="1" y="80" width="59" height="34" fill="var(--stripe-orange)"/>
    <rect x="1" y="137" width="59" height="48" fill="var(--stripe-orange)"/>
    <rect x="1" y="250" width="59" height="48" fill="var(--stripe-orange)"/>
    <rect x="1" y="363" width="59" height="48" fill="var(--stripe-orange)"/>
    <rect x="1" y="476" width="59" height="48" fill="var(--stripe-orange)"/>
    <rect x="1" y="583" width="59" height="44" fill="var(--stripe-orange)"/>
  </svg>

  <ul class="contact">
    <li class="contact-name">Corin Ashdale</li>
    <li class="contact-phone">Phone: 999-999-9999</li>
    <li class="contact-email-label">Email:</li>
    <li class="contact-email">cashdale@mail.example</li>
    <li class="contact-web">www.velmargear.example</li>
  </ul>
</main>
</body>
</html>
```